Classy, Elegant, Simple Business Card Design

Looking to have a classy, simple, and elegant design. Want a top notch designed business card. I really like the look of the new brivo credit card. I also like the design I attached. I am trying to reach 21-29 year old females for booking us for there wedding or event. We offer Disc Jockey Service, Photo Booth Rentals, and Uplighting .

Target Market(s)

21-28 year old females

Contact Information for Business Card

Has to have logo, website, email, and phone number

Font styles to use
Other font styles liked:
• open to font choice, modern, clean
Designer to choose
33a6d7
0791cd
0555a3
ffffff

Requirements
Must have
• Has to have logo, website, email, and phone number
Nice to have
• I really like the design of the new brivo credit card. I also included my logo and some designs I like
Should not have
• clutter or too much info

```html
<!DOCTYPE html>
<html lang="en">
<head>
<meta charset="utf-8">
<title>Tidelight Event Group – Business Card</title>
<link href="https://fonts.googleapis.com/css2?family=Jost:wght@400&family=Open+Sans:wght@400;600&display=swap" rel="stylesheet">
<style>
  :root {
    --stage: #d9dbde;
    --navy: #0f2f57;
    --navy-deep: #0b2646;
    --blue: #0791cd;
    --blue-dark: #0555a3;
    --sky: #33a6d7;
    --white: #ffffff;
    --ink: #1a1a1a;
    --muted: #8b97a6;
  }
  * { box-sizing: border-box; margin: 0; padding: 0; }
  html, body { width: 1200px; height: 1021px; overflow: hidden; }
  body {
    background: var(--stage);
    font-family: "Open Sans", sans-serif;
    position: relative;
  }
  .card {
    position: absolute;
    left: 290px;
    width: 620px;
    height: 354px;
    border-radius: 4px;
    box-shadow: 0 6px 18px rgba(0,0,0,0.18);
    overflow: hidden;
  }
  /* Back of card */
  .card--back {
    top: 110px;
    background: linear-gradient(135deg, var(--navy) 0%, var(--navy-deep) 100%);
  }
  .card--back .wordmark {
    position: absolute;
    left: 150px;
    top: 148px;
    color: var(--white);
  }
  .wordmark {
    font-family: "Jost", sans-serif;
    font-weight: 400;
    text-transform: uppercase;
    line-height: 1.1;
  }
  .wordmark__name { display: block; font-size: 34px; letter-spacing: 1px; }
  .wordmark__sub { display: block; font-size: 12px; letter-spacing: 9px; padding-left: 2px; }
  .card--back .accent {
    position: absolute;
    right: 0; top: 0; bottom: 0;
    width: 6px;
    background: var(--sky);
  }
  /* Front of card */
  .card--front {
    top: 556px;
    background: var(--white);
  }
  .holder {
    position: absolute;
    left: 50px;
    top: 118px;
    width: 230px;
    text-align: right;
  }
  .holder__name { color: var(--blue-dark); font-weight: 600; font-size: 22px; }
  .holder__role { color: var(--ink); font-size: 15px; margin-top: 2px; }
  .details {
    position: absolute;
    left: 330px;
    top: 52px;
    width: 270px;
  }
  .details .wordmark { color: var(--blue-dark); }
  .details .wordmark__name { font-size: 27px; }
  .details .wordmark__sub { font-size: 10px; letter-spacing: 7px; }
  .address { margin-top: 28px; font-size: 15px; line-height: 1.35; color: var(--ink); }
  .contacts { list-style: none; margin-top: 12px; font-size: 15px; color: var(--ink); }
  .contacts li { display: flex; align-items: center; gap: 8px; line-height: 1.55; }
  .contacts svg { width: 15px; height: 15px; flex: none; fill: none; stroke: var(--blue); stroke-width: 1.8; }
</style>
</head>
<body>
  <section class="card card--back" aria-label="Card back">
    <div class="wordmark">
      <span class="wordmark__name">Tidelight</span>
      <span class="wordmark__sub">Event Group</span>
    </div>
    <div class="accent"></div>
  </section>

  <section class="card card--front" aria-label="Card front">
    <div class="holder">
      <p class="holder__name">Daniel Carter</p>
      <p class="holder__role">Founder</p>
    </div>
    <div class="details">
      <div class="wordmark">
        <span class="wordmark__name">Tidelight</span>
        <span class="wordmark__sub">Event Group</span>
      </div>
      <p class="address">48 Harbor Lane, Suite 310<br>Bayview, Florida, 33010</p>
      <ul class="contacts">
        <li>
          <svg viewBox="0 0 16 16" aria-hidden="true"><path d="M4 1.5l2.5 3-1.5 1.8c.8 1.8 2.2 3.2 4 4l1.8-1.5 3 2.5-1.5 2.2C7.5 13.5 2.5 8.5 1.8 3.3z"/></svg>
          (555) 014-2290
        </li>
        <li>
          <svg viewBox="0 0 16 16" aria-hidden="true"><rect x="1.5" y="3.5" width="13" height="9"/><path d="M1.5 3.5l6.5 5 6.5-5"/></svg>
          daniel@tidelightevents.com
        </li>
        <li>
          <svg viewBox="0 0 16 16" aria-hidden="true"><circle cx="8" cy="8" r="6.5"/><path d="M1.5 8h13M8 1.5c-2.5 3-2.5 10 0 13M8 1.5c2.5 3 2.5 10 0 13"/></svg>
          www.tidelightevents.com
        </li>
      </ul>
    </div>
  </section>
</body>
</html>
```